Vord Plix Business Cards
Vord Plix Stationary
Professional
Harold (Hal) Brennick
Director
Asia Pacific and Middle East
harold@vord-plix.com
www.vord-plix.com
I have thought about utilizing the four corners of the business card by putting name, phone, email address and url.
Possible full bleed.
would also like the back to say the following:
Oil&Gas Emergency Response Planning and Consulting.

```html
<!DOCTYPE html>
<html lang="en">
<head>
<meta charset="utf-8">
<title>Vord Plix Business Cards</title>
<link href="https://fonts.googleapis.com/css2?family=Open+Sans:ital,wght@0,400;0,600;0,700;1,400&family=Josefin+Sans:wght@400&display=swap" rel="stylesheet">
<style>
  :root{
    --board:#3a3a3a;
    --board-light:#4a4a4a;
    --card-light:#ffffff;
    --card-dark:#2f2d2e;
    --ink-dark:#3d3d3d;
    --ink-muted:#8a8a8a;
    --ink-light:#d6d6d6;
    --accent:#f07f1a;
    --accent-deep:#e0560f;
    --accent-soft:#f9b233;
    --swoosh:#9a9a9a;
    --label:#e2e2e2;
    --logo-box:#000000;
  }
  *{box-sizing:border-box;margin:0;padding:0}
  html,body{width:1200px;height:809px;overflow:hidden}
  body{
    background:radial-gradient(circle at 50% 40%,var(--board-light),var(--board) 75%);
    font-family:"Open Sans",Arial,sans-serif;
    position:relative;
  }
  .card{
    position:absolute;width:435px;height:293px;border-radius:16px;overflow:hidden;
    box-shadow:0 2px 6px rgba(0,0,0,.45);
  }
  .card--light{background:var(--card-light)}
  .card--dark{background:var(--card-dark)}
  .front-a{left:74px;top:43px}
  .front-b{left:629px;top:43px}
  .back-a{left:74px;top:420px}
  .back-b{left:629px;top:420px}

  .card-label{
    position:absolute;width:435px;text-align:center;
    font-family:"Josefin Sans",Arial,sans-serif;font-variant:small-caps;
    font-size:19px;letter-spacing:3px;color:var(--label);
  }
  .label-front-a{left:74px;top:353px}
  .label-front-b{left:629px;top:353px}
  .label-back-a{left:74px;top:730px}
  .label-back-b{left:629px;top:730px}

  .brand{
    position:absolute;left:18px;top:128px;width:250px;
    display:flex;align-items:center;gap:10px;
  }
  .brand-dot{width:26px;height:26px;border-radius:50%;background:var(--accent);flex:none}
  .brand-name{font-weight:700;font-size:34px;letter-spacing:1px;color:var(--ink-dark);line-height:1}
  .logo-box{position:absolute;left:14px;top:58px;width:262px;height:150px;background:var(--logo-box)}
  .front-b .brand-name{color:#ffffff}

  .divider{position:absolute;left:281px;top:62px;width:1px;height:142px;background:#d0d0d0}
  .front-b .divider{background:#6a6a6a}

  .contact{position:absolute;left:292px;top:66px;width:140px}
  .contact-name{font-size:10.5px;color:var(--accent);font-weight:600;white-space:nowrap}
  .contact-role{font-size:9px;color:var(--ink-muted);margin-bottom:14px}
  .contact-line{display:flex;align-items:center;gap:6px;font-size:9px;color:var(--ink-muted);height:20px;white-space:nowrap}
  .front-b .contact-line{color:var(--ink-light)}
  .contact-line svg{flex:none}

  .swoosh{position:absolute;left:0;bottom:0}

  .tagline{
    position:absolute;left:0;top:110px;width:100%;text-align:center;
    font-style:italic;font-size:11px;color:var(--ink-dark);
  }
  .back-b .tagline{color:var(--ink-light)}
</style>
</head>
<body>

<svg width="0" height="0" style="position:absolute">
  <defs>
    <linearGradient id="band-grad" x1="0" y1="0" x2="0" y2="1">
      <stop offset="0" stop-color="#f9b233"/>
      <stop offset="0.5" stop-color="#f07f1a"/>
      <stop offset="1" stop-color="#e0560f"/>
    </linearGradient>
    <linearGradient id="gray-grad" x1="0" y1="0" x2="1" y2="0">
      <stop offset="0" stop-color="#7a7a7a"/>
      <stop offset="0.5" stop-color="#d8d8d8"/>
      <stop offset="1" stop-color="#7a7a7a"/>
    </linearGradient>
  </defs>
</svg>

<!-- Front A -->
<section class="card card--light front-a">
  <div class="brand"><span class="brand-dot"></span><span class="brand-name">VORD PLIX</span></div>
  <div class="divider"></div>
  <div class="contact">
    <div class="contact-name">Harold (Hal) Brennick</div>
    <div class="contact-role">Director</div>
    <div class="contact-line"><svg width="9" height="9" viewBox="0 0 10 10"><path d="M2 1h2l1 2.5-1.3 1a6 6 0 0 0 2.8 2.8l1-1.3L10 7v2c0 .6-.4 1-1 1A9 9 0 0 1 0 1c0-.6.4-1 1-1z" fill="var(--accent)"/></svg>+971 50 214 3086</div>
    <div class="contact-line"><svg width="9" height="9" viewBox="0 0 10 10"><rect x="2.5" y="0" width="5" height="10" rx="1" fill="var(--accent)"/><rect x="3.5" y="1.5" width="3" height="6" fill="#fff"/></svg>+66 81 362 9048</div>
    <div class="contact-line"><svg width="9" height="9" viewBox="0 0 10 10"><rect x="0" y="2" width="10" height="7" fill="var(--accent)"/><path d="M0 2l5 4 5-4" stroke="#fff" fill="none"/></svg>harold@vord-plix.com</div>
    <div class="contact-line"><svg width="9" height="9" viewBox="0 0 10 10"><circle cx="5" cy="5" r="4.5" fill="var(--accent)"/><path d="M.5 5h9M5 .5v9" stroke="#fff" stroke-width=".8"/></svg>www.vord-plix.com</div>
  </div>
  <svg class="swoosh" width="435" height="75" viewBox="0 0 435 75">
    <path d="M0 20 Q217 -8 435 20 L435 75 L0 75Z" fill="url(#gray-grad)"/>
    <path d="M0 34 Q217 8 435 32 L435 75 L0 75Z" fill="url(#band-grad)"/>
  </svg>
</section>
<div class="card-label label-front-a">Business Card Front Option A</div>

<!-- Front B -->
<section class="card card--dark front-b">
  <div class="logo-box"></div>
  <div class="brand"><span class="brand-dot"></span><span class="brand-name">VORD PLIX</span></div>
  <div class="divider"></div>
  <div class="contact">
    <div class="contact-name">Harold (Hal) Brennick</div>
    <div class="contact-role">Director</div>
    <div class="contact-line"><svg width="9" height="9" viewBox="0 0 10 10"><path d="M2 1h2l1 2.5-1.3 1a6 6 0 0 0 2.8 2.8l1-1.3L10 7v2c0 .6-.4 1-1 1A9 9 0 0 1 0 1c0-.6.4-1 1-1z" fill="var(--accent)"/></svg>+971 50 214 3086</div>
    <div class="contact-line"><svg width="9" height="9" viewBox="0 0 10 10"><rect x="2.5" y="0" width="5" height="10" rx="1" fill="var(--accent)"/><rect x="3.5" y="1.5" width="3" height="6" fill="#2f2d2e"/></svg>+66 81 362 9048</div>
    <div class="contact-line"><svg width="9" height="9" viewBox="0 0 10 10"><rect x="0" y="2" width="10" height="7" fill="var(--accent)"/><path d="M0 2l5 4 5-4" stroke="#2f2d2e" fill="none"/></svg>harold@vord-plix.com</div>
    <div class="contact-line"><svg width="9" height="9" viewBox="0 0 10 10"><circle cx="5" cy="5" r="4.5" fill="var(--accent)"/><path d="M.5 5h9M5 .5v9" stroke="#2f2d2e" stroke-width=".8"/></svg>www.vord-plix.com</div>
  </div>
  <svg class="swoosh" width="435" height="75" viewBox="0 0 435 75">
    <path d="M0 20 Q217 -8 435 20 L435 75 L0 75Z" fill="url(#gray-grad)"/>
    <path d="M0 34 Q217 8 435 32 L435 75 L0 75Z" fill="url(#band-grad)"/>
  </svg>
</section>
<div class="card-label label-front-b">Business Card Front Option B</div>

<!-- Back A -->
<section class="card card--light back-a">
  <p class="tagline">Oil &amp; Gas Emergency Response Planning and Consulting.</p>
</section>
<div class="card-label label-back-a">Business Card Back Option A</div>

<!-- Back B -->
<section class="card card--dark back-b">
  <p class="tagline">Oil &amp; Gas Emergency Response Planning and Consulting.</p>
</section>
<div class="card-label label-back-b">Business Card Back Option B</div>

</body>
</html>
```